Maple Lantern Business Card

Colors can be blue, grey and white as you see in the attached logo. Needs to have a spot for name, title, phone, email, address, and website. There also needs to be a spot for an agent's picture.

Contact Information for Business Card

See project description.

Colors

Designer to choose colors to be used in the design.

```html
<!DOCTYPE html>
<html lang="en">
<head>
<meta charset="utf-8">
<title>Maple Lantern Business Card</title>
<link href="https://fonts.googleapis.com/css2?family=Montserrat:wght@400;500;600;700&display=swap" rel="stylesheet">
<style>
  :root {
    --stage: #000000;
    --white: #ffffff;
    --slate: #5c6068;
    --slate-mid: #6e7a92;
    --sky: #a9b9de;
    --blue: #3a78c2;
    --blue-light: #5ea3dc;
    --charcoal: #58595b;
    --photo-top: #7f97c9;
    --photo-mid: #3f5f92;
    --photo-deep: #1d2c48;
    --frame: rgba(255, 255, 255, 0.7);
  }
  * { margin: 0; padding: 0; box-sizing: border-box; }
  html, body {
    width: 900px; height: 1200px; overflow: hidden;
    background: var(--stage);
    font-family: "Montserrat", Arial, sans-serif;
  }
  .card {
    position: absolute; left: 82px; width: 733px; height: 430px;
    border-radius: 22px; overflow: hidden;
  }
  .card--front {
    top: 137px;
    background: linear-gradient(90deg, var(--slate) 0%, var(--slate-mid) 45%, var(--sky) 100%);
    color: var(--white);
  }
  .card--back { top: 632px; background: var(--white); }

  .agent-photo {
    position: absolute; left: 390px; top: 28px; width: 328px; height: 388px;
    border-radius: 14px;
    background: linear-gradient(180deg, var(--photo-top) 0%, var(--photo-mid) 45%, var(--photo-deep) 100%);
    border: 2px dashed var(--frame);
  }

  .front-brand {
    position: absolute; left: 45px; top: 125px; width: 290px;
    text-align: center; font-weight: 700; font-size: 30px;
    letter-spacing: 0.5px; text-transform: uppercase;
  }
  .agent-name {
    position: absolute; left: 45px; top: 208px;
    font-size: 23px; font-weight: 600;
  }
  .agent-title {
    position: absolute; left: 45px; top: 237px;
    font-size: 18px; font-weight: 400;
  }
  .rule {
    position: absolute; left: 45px; width: 287px; height: 1px;
    background: rgba(255,255,255,0.85);
  }
  .rule--top { top: 267px; }
  .rule--bottom { top: 351px; }
  .contact-list { position: absolute; left: 45px; top: 275px; list-style: none; }
  .contact-list li {
    display: flex; align-items: center; height: 24px;
    font-size: 16.5px; font-weight: 400;
  }
  .contact-list svg { width: 16px; height: 16px; margin-right: 10px; fill: var(--white); }
  .office-address {
    position: absolute; left: 45px; top: 358px;
    font-size: 16px; line-height: 23px; font-style: normal;
  }

  .back-shapes { position: absolute; inset: 0; }
  .back-brand {
    position: absolute; left: 0; right: 0; top: 232px;
    text-align: center; color: var(--blue);
    font-weight: 700; font-size: 34px; text-transform: uppercase; letter-spacing: 0.5px;
  }
</style>
</head>
<body>
  <section class="card card--front">
    <div class="agent-photo" role="img" aria-label="Photo placeholder: portrait of the agent in a dark suit"></div>

    <div class="front-brand">Maple Lantern</div>

    <h1 class="agent-name">Daniel Whitford</h1>
    <p class="agent-title">Managing Director</p>
    <div class="rule rule--top"></div>

    <ul class="contact-list">
      <li>
        <svg viewBox="0 0 24 24" aria-hidden="true"><path d="M6.6 10.8c1.4 2.8 3.8 5.1 6.6 6.6l2.2-2.2c.3-.3.7-.4 1-.2 1.1.4 2.3.6 3.6.6.6 0 1 .4 1 1V20c0 .6-.4 1-1 1C10.6 21 3 13.4 3 4c0-.6.4-1 1-1h3.5c.6 0 1 .4 1 1 0 1.3.2 2.5.6 3.6.1.3 0 .7-.2 1z"/></svg>
        555-013-4872
      </li>
      <li>
        <svg viewBox="0 0 24 24" aria-hidden="true"><path d="M2 5h20v14H2z M3.5 6.5 12 13l8.5-6.5" fill="none" stroke="#fff" stroke-width="2"/><path d="M2 5h20l-10 8z"/></svg>
        daniel@maplelantern.com
      </li>
      <li>
        <svg viewBox="0 0 24 24" aria-hidden="true"><g fill="none" stroke="#fff" stroke-width="1.8"><circle cx="12" cy="12" r="9"/><ellipse cx="12" cy="12" rx="4" ry="9"/><path d="M3 12h18M4.5 7.5h15M4.5 16.5h15"/></g></svg>
        www.maplelantern.com
      </li>
    </ul>
    <div class="rule rule--bottom"></div>

    <address class="office-address">
      418 Cedar Ridge Road<br>
      Suite 210, Millbrook, MI 49021
    </address>
  </section>

  <section class="card card--back">
    <svg class="back-shapes" viewBox="0 0 733 430" width="733" height="430" aria-hidden="true">
      <polygon points="0,0 100,0 0,62" fill="var(--charcoal)"/>
      <polygon points="0,70 112,0 310,0 0,100" fill="var(--blue)"/>
      <polygon points="0,100 180,40 0,140" fill="var(--blue-light)"/>
      <polygon points="733,265 733,385 580,430 650,430" fill="var(--blue-light)"/>
      <polygon points="733,330 733,395 620,430 575,430" fill="var(--blue)"/>
      <polygon points="733,395 733,430 655,430" fill="var(--charcoal)"/>
    </svg>
    <div class="back-brand">Maple Lantern</div>
  </section>
</body>
</html>
```